SupplierLens720 Business Card Design

Design double sided premium business card – we will print on heavy card stock. Would like an edgy eye-catchcing card in Spot UV and/or Embossed or Foil. Something that will be memorable to our clients and new prospects
PLEASE NOTE: I have attached a word document with a more detailed overview, instructions and ideas. please review this and send a message if you have any questions

Industry/Entity Type

Financial Service

Contact Information for Business Card

would prefer to have Spot UV and/or Embossed or Foil (but no gold or silver- if you do foil only colored)

Requirements
Must have
• 1) Tagline: Redefining the way you search, qualify & manage vendors
• 2) Color Front of Card: Open to any color combo
• 3) Color on back of card: would prefer white so the contact information is easy to read
• 4) A creative design aspect.. the eye is an idea but not imperative. if you have another creative idea that represents supplierlens720 please do so. We are open to other design ideas.
Nice to have
• If you can use the words on the card as shown on my instruction document that would be nice ... I like example 1 and 1A on the logo ideas I put on the instruction document.
Should not have
• 1) We DO NOT want an all black card. (front and back)
• 2) We do not want a basic card that has the logo on front- we want some type of design incorporated on the card. - we would like something creative to grab attention.
• Note: I have attached examples of other card designs on our instruction document we attached please review and create something eye-catching like these.

```html
<!DOCTYPE html>
<html lang="en">
<head>
<meta charset="utf-8">
<title>SupplierLens720 Business Card</title>
<link rel="stylesheet" href="https://fonts.googleapis.com/css2?family=Open+Sans:wght@400;600&display=swap">
<style>
  :root {
    --bg: #2a2a2a;
    --card-black: #151515;
    --card-white: #ffffff;
    --brand-blue: #0b57a4;
    --brand-green: #8cc63f;
    --logo-blue: #2f7fd0;
    --text-dark: #222222;
    --text-soft: #9aa7b5;
    --web-blue: #2d5f99;
  }
  * { box-sizing: border-box; margin: 0; padding: 0; }
  html, body {
    width: 1200px; height: 716px; overflow: hidden;
    background: var(--bg);
    font-family: "Open Sans", sans-serif;
  }
  .canvas { position: relative; width: 1200px; height: 716px; }
  .card {
    position: absolute; top: 204px;
    width: 540px; height: 309px;
    border-radius: 22px; overflow: hidden;
  }
  .card-front { left: 40px; background: var(--card-black); }
  .card-back { left: 620px; background: var(--card-white); }

  .brand-name {
    position: absolute;
    font-weight: 600;
    letter-spacing: 0.5px;
    color: var(--logo-blue);
    white-space: nowrap;
  }
  .card-front .brand-name { left: 0; right: 0; top: 78px; text-align: center; font-size: 36px; }
  .tagline {
    position: absolute; left: 60px; right: 60px; top: 136px;
    text-align: center; font-size: 13px; line-height: 1.4;
    color: var(--text-soft);
  }
  .website {
    position: absolute; left: 0; right: 0; top: 186px;
    text-align: center; font-size: 14px; letter-spacing: 3px;
    color: var(--web-blue);
  }

  .card-back .brand-name { left: 40px; top: 122px; font-size: 25px; color: var(--brand-blue); }
  .divider {
    position: absolute; left: 335px; top: 80px;
    width: 2px; height: 150px; background: var(--brand-blue);
  }
  .holder { position: absolute; left: 356px; top: 82px; }
  .holder-name { font-size: 28px; color: var(--text-dark); line-height: 1.1; white-space: nowrap; }
  .holder-title { font-size: 14px; color: var(--logo-blue); margin-top: 2px; }
  .contacts { list-style: none; margin-top: 16px; }
  .contacts li {
    display: flex; align-items: center; gap: 8px;
    font-size: 14px; color: var(--text-dark); margin-bottom: 6px;
    white-space: nowrap;
  }
  .contacts svg { width: 13px; height: 13px; fill: var(--brand-blue); flex: none; }
  .wave { position: absolute; left: 0; bottom: 0; width: 540px; height: 309px; }
</style>
</head>
<body>
<div class="canvas">
  <section class="card card-front">
    <svg class="wave" viewBox="0 0 540 309" aria-hidden="true">
      <path fill="var(--brand-green)" d="M150 252 C 290 270, 430 272, 540 270 L540 294 C 450 282, 320 274, 150 252 Z"/>
      <path fill="var(--brand-blue)" d="M0 240 C 50 248, 110 250, 170 256 C 320 274, 450 282, 540 300 L540 309 L0 309 Z"/>
    </svg>
    <div class="brand-name">SupplierLens720</div>
    <p class="tagline">Redefining the way you search, qualify &amp; manage vendors</p>
    <div class="website">www.yourwebsite.com</div>
  </section>

  <section class="card card-back">
    <svg class="wave" viewBox="0 0 540 309" aria-hidden="true">
      <path fill="var(--brand-green)" d="M150 222 C 290 246, 430 250, 540 252 L540 286 C 450 262, 320 250, 150 222 Z"/>
      <path fill="var(--brand-blue)" d="M0 205 C 50 215, 110 218, 170 228 C 320 252, 450 262, 540 290 L540 309 L0 309 Z"/>
    </svg>
    <div class="brand-name">SupplierLens720</div>
    <div class="divider"></div>
    <div class="holder">
      <div class="holder-name">Your Name</div>
      <div class="holder-title">Job Title</div>
      <ul class="contacts">
        <li><svg viewBox="0 0 16 16"><path d="M2 6c0-2 2-3 6-3s6 1 6 3v1h-3V5.5H5V7H2z M3 8h10l1 5H2z"/></svg>000 000 0000</li>
        <li><svg viewBox="0 0 16 16"><path d="M1 3h14v10H1z M2 4l6 5 6-5" stroke="#fff" stroke-width="1"/></svg>youremail@xyz.com</li>
        <li><svg viewBox="0 0 16 16"><path d="M8 1a5 5 0 0 1 5 5c0 4-5 9-5 9S3 10 3 6a5 5 0 0 1 5-5z"/><circle cx="8" cy="6" r="2" fill="#fff"/></svg>Your Address here</li>
      </ul>
    </div>
  </section>
</div>
</body>
</html>
```